Business Card Design Project- Removalist

I would like to surprise my husband to be with a different type of wedding present. His brother (who he owned a removalist business with) suddenly passed away from cancer recently and he has changed his business name to 'TQB' (which stands for Keeping Ted Strong; but the full name doesn't need to be on the business card as it is more of a personal business name). To celebrate the new business I would like to get him some business cards made.
I would like the business name to be listed as 'TQB' and somewhere on the card I would like 'Sydney wide removals and relocation services'. I would like it to be obvious from the front of the card that it is a removalist business card. If a truck or some other feature that makes it look like a removalist business card could added it would be appreciated.
I don't mind what colours are used, but I would like the colour blue to feature somewhere in the design. It can be bright and fun, which is how Ted was.
I will also need the company's email address and phone number listed
The email address is: tqbmoving@brisketmail.example
The contact number is: 0418 902 364
I don't need a contact name listed on the card, but perhaps 'Owned and operated by the Pemberton family' could be added near the contact details in small font.
Thank you very much for considering this project!
Kind regards,
Fiona
Updates
Could you please change the mobile contact number to 0418 902 364. This is the only contact phone number required on the card now.
Thank you!
Industry/Entity Type
Wedding
Look and feel
Each slider illustrates characteristics of the customer's brand and the style your logo design should communicate.

```html
<!DOCTYPE html>
<html lang="en">
<head>
<meta charset="utf-8">
<title>TQB Business Cards</title>
<link href="https://fonts.googleapis.com/css2?family=Open+Sans:wght@400;600;700;800&display=swap" rel="stylesheet">
<style>
  :root {
    --page: #e9e6e1;
    --card: #f8f4ea;
    --ink: #1f1d1a;
    --ink-soft: #4a4640;
    --brand-grey: #6b665f;
    --brand-faint: #dcd6cb;
    --cyan: #1fd0da;
    --blue: #1a86c6;
    --blue-deep: #1667b3;
    --swoosh-light: #c9f1f4;
    --truck-tone: #e6e0d4;
    --truck-tone-dark: #cfc7b8;
  }
  * { box-sizing: border-box; margin: 0; padding: 0; }
  html, body {
    width: 1200px;
    height: 796px;
    overflow: hidden;
    background: var(--page);
    font-family: "Open Sans", Arial, sans-serif;
  }
  .sheet {
    position: relative;
    width: 1200px;
    height: 796px;
  }
  .card {
    position: absolute;
    width: 600px;
    height: 343px;
    background: var(--card);
    overflow: hidden;
    box-shadow: 0 6px 18px rgba(0,0,0,0.15);
  }
  .card--back { left: 520px; top: 32px; }
  .card--front { left: 80px; top: 421px; }

  .swoosh {
    position: absolute;
    inset: 0;
    width: 100%;
    height: 100%;
  }

  /* Back */
  .back-name {
    position: absolute;
    left: 86px;
    top: 22px;
    font-size: 56px;
    font-weight: 800;
    letter-spacing: 1px;
    color: var(--brand-faint);
  }
  .contact {
    position: absolute;
    left: 78px;
    top: 96px;
    font-size: 12px;
    line-height: 16px;
    color: var(--ink-soft);
  }

  /* Front */
  .truck-art {
    position: absolute;
    left: 100px;
    top: 110px;
    width: 220px;
    height: 130px;
    border-radius: 14px;
    background: linear-gradient(180deg, var(--truck-tone) 0%, var(--truck-tone-dark) 100%);
    opacity: 0.7;
  }
  .brand-name {
    position: absolute;
    left: 106px;
    top: 36px;
    font-size: 96px;
    line-height: 1;
    font-weight: 800;
    letter-spacing: 2px;
    color: var(--brand-grey);
  }
  .tagline {
    position: absolute;
    left: 96px;
    top: 150px;
    font-size: 17px;
    font-weight: 700;
    color: var(--ink);
  }
</style>
</head>
<body>
<main class="sheet">

  <section class="card card--back" aria-label="Business card back">
    <div class="back-name">TQB</div>
    <div class="contact">
      <p class="contact__email">Email address: tqbmoving@brisketmail.example</p>
      <p class="contact__phone">Contact number: 0418 902 364</p>
    </div>
    <svg class="swoosh" viewBox="0 0 600 343" aria-hidden="true">
      <defs>
        <linearGradient id="backBlue" x1="0" y1="0" x2="1" y2="1">
          <stop offset="0" stop-color="var(--cyan)"/>
          <stop offset="1" stop-color="var(--blue-deep)"/>
        </linearGradient>
        <linearGradient id="backFade" x1="0" y1="0" x2="1" y2="0">
          <stop offset="0" stop-color="var(--swoosh-light)" stop-opacity="0"/>
          <stop offset="0.5" stop-color="var(--swoosh-light)" stop-opacity="0.9"/>
          <stop offset="1" stop-color="var(--cyan)"/>
        </linearGradient>
      </defs>
      <path d="M0,180 C160,300 420,290 600,150 L600,200 C420,320 180,330 0,300 Z" fill="url(#backFade)"/>
      <path d="M200,343 C380,320 510,260 600,190 L600,343 Z" fill="url(#backBlue)"/>
    </svg>
  </section>

  <section class="card card--front" aria-label="Business card front">
    <div class="truck-art" role="img" aria-label="Faint photograph of a removals truck"></div>
    <div class="brand-name">TQB</div>
    <p class="tagline">Sydney wide removals and relocation services</p>
    <svg class="swoosh" viewBox="0 0 600 343" aria-hidden="true">
      <defs>
        <linearGradient id="frontBlue" x1="0" y1="0" x2="1" y2="1">
          <stop offset="0" stop-color="var(--cyan)"/>
          <stop offset="0.6" stop-color="var(--blue)"/>
          <stop offset="1" stop-color="var(--blue-deep)"/>
        </linearGradient>
        <linearGradient id="frontFade" x1="0" y1="0" x2="1" y2="0">
          <stop offset="0" stop-color="var(--swoosh-light)" stop-opacity="0"/>
          <stop offset="0.55" stop-color="var(--swoosh-light)" stop-opacity="0.9"/>
          <stop offset="1" stop-color="var(--cyan)"/>
        </linearGradient>
      </defs>
      <path d="M0,200 C170,300 420,290 600,130 L600,185 C420,320 180,335 0,300 Z" fill="url(#frontFade)"/>
      <path d="M150,343 C360,320 500,260 600,170 L600,343 Z" fill="url(#frontBlue)"/>
    </svg>
  </section>

</main>
</body>
</html>
```